Oral Surgery Office Referral Forms and Stationary Designs

I want something like the ones you made for Harbor Crest Oral Surgery. Please use my logo for color scheme and refer to this URL:

https://www.plornexa.example/design/552031

I would also like similar business cards with appointment date/time as well as stationaries.

Target Market(s)

Referring dentists

Industry/Entity Type

Office

Font styles to use
Serif

Requirements
Must have
• same as harbor crest oral surgery forms, I will add or delete items as I find fit once the design is ready

```html
<!DOCTYPE html>
<html lang="en">
<head>
<meta charset="utf-8">
<title>Dr. Lennart Oral Surgeon – Stationery</title>
<link rel="stylesheet" href="https://fonts.googleapis.com/css2?family=Nunito+Sans:wght@400&family=Questrial&family=Roboto:wght@400;500&display=swap">
<style>
  :root {
    --backdrop: #dcdcdc;
    --paper: #f7f7f7;
    --ink: #444444;
    --body-ink: #555555;
    --leaf: #2ee58a;
    --flap: #444444;
    --flap-ink: #ffffff;
    --signature: #c8d2e6;
  }
  * { margin: 0; padding: 0; box-sizing: border-box; }
  html, body { width: 1200px; height: 877px; overflow: hidden; }
  body { background: var(--backdrop); position: relative; font-family: "Questrial", sans-serif; color: var(--ink); }
  address { font-style: normal; }

  .sheet { position: absolute; background: var(--paper); }

  .brand { position: absolute; display: flex; align-items: center; gap: 4px; }
  .brand-dot { width: 38px; height: 38px; border-radius: 50%; background: var(--leaf); flex: none; }
  .brand-name { font-family: "Nunito Sans", sans-serif; font-weight: 400; color: var(--ink); font-size: 21px; line-height: 20px; white-space: nowrap; }
  .brand-name span { display: block; }

  /* Letterhead */
  .letterhead { left: 61px; top: 64px; width: 527px; height: 742px; }
  .letterhead .brand { left: 45px; top: 54px; }
  .contact { position: absolute; right: 42px; top: 54px; text-align: right; font-family: "Roboto", sans-serif; font-size: 8px; line-height: 9.6px; color: var(--ink); }
  .contact .firm { font-weight: 500; }
  .contact .lines { margin-top: 4px; }
  .contact .lines div { display: flex; justify-content: flex-end; align-items: center; gap: 4px; line-height: 10.5px; }
  .contact svg { width: 7px; height: 7px; fill: var(--leaf); }
  .salutation { position: absolute; left: 47px; top: 207px; font-size: 13.6px; }
  .body-copy { position: absolute; left: 47px; top: 250px; width: 440px; font-size: 7.6px; line-height: 11.4px; color: var(--body-ink); }
  .body-copy p + p { margin-top: 11.4px; }
  .closing { position: absolute; left: 47px; top: 486px; font-size: 7.6px; color: var(--body-ink); }
  .signature { position: absolute; left: 41px; top: 520px; width: 94px; height: 38px; background: var(--signature); border-radius: 4px; }

  /* Envelope back */
  .envelope-back { left: 614px; top: 296px; width: 531px; height: 241px; }
  .flap { position: absolute; left: 0; top: 0; width: 531px; height: 75px; }
  .envelope-back .brand { left: 224px; top: 21px; gap: 3px; }
  .envelope-back .brand-dot { width: 22px; height: 22px; }
  .envelope-back .brand-name { font-size: 11px; line-height: 11px; color: var(--flap-ink); }

  /* Envelope front */
  .envelope-front { left: 614px; top: 565px; width: 533px; height: 242px; }
  .envelope-front .brand { left: 18px; top: 31px; }
  .return-address { position: absolute; left: 60px; top: 94px; font-family: "Roboto", sans-serif; font-size: 8px; line-height: 9.6px; color: var(--ink); }
  .return-address .firm { font-weight: 500; }
</style>
</head>
<body>

  <section class="sheet letterhead">
    <div class="brand">
      <span class="brand-dot"></span>
      <span class="brand-name"><span>DR.</span><span>LENNART</span><span>Oral Surgeon</span></span>
    </div>

    <address class="contact">
      <div class="firm">Dr. Lennart Oral Surgeon</div>
      <div>4120 Tidewater Road</div>
      <div>Juneau, Alaska 99801</div>
      <div class="lines">
        <div>(555) 014.2290
          <svg viewBox="0 0 10 10"><path d="M2 0.5 L3.8 2.6 L2.9 3.8 C3.6 5.2 4.8 6.4 6.2 7.1 L7.4 6.2 L9.5 8 L8.2 9.5 C4.2 9.2 0.8 5.8 0.5 1.8 Z"/></svg>
        </div>
        <div>info@drlennart.example
          <svg viewBox="0 0 10 10"><path d="M0 2 H10 V8.5 H0 Z M0.6 2.4 L5 5.6 L9.4 2.4" stroke="#f7f7f7" stroke-width="0.8"/></svg>
        </div>
        <div>www.drlennart.example
          <svg viewBox="0 0 10 10"><circle cx="5" cy="5" r="5"/></svg>
        </div>
      </div>
    </address>

    <p class="salutation">Dear Mr. Aldren,</p>

    <div class="body-copy">
      <p>Lorem ipsum dolor sit amet, consectetur adipiscing elit. Donec orci purus, luctus vitae dignissim eu, iaculis sed purus. Vivamus faucibus, ipsum nec aliquet viverra, leo mauris condimentum ligula, sit amet sagittis enim ligula quis arcu. Nam egestas tortor id nisi porttitor mattis. In tortor ante, ultricies in suscipit a, tempus non massa. Vivamus et auctor mi. Fusce vel massa nulla. Phasellus nec eros mauris, et scelerisque orci.</p>
      <p>Donec malesuada orci vitae nulla accumsan porta a id massa. Quisque accumsan iaculis magna sit amet fringilla. Maecenas consequat, magna eget tincidunt semper, odio nibh rutrum mi, id feugiat ante nisi eu risus. Vestibulum nunc orci, rhoncus a placerat in, ultricies in mi. Cras mattis varius eros, vel fringilla nisi suscipit eget. Quisque scelerisque sagittis nulla at porttitor.</p>
      <p>Sed id augue vitae urna euismod commodo aliquet a quam. Pellentesque arcu velit, cursus et malesuada ut, consequat et diam. Nullam erat sem, rhoncus id ullamcorper vitae, rhoncus et arcu. In ultricies ultricies nulla, ut rutrum nisi iaculis at. Donec eu magna a metus ornare faucibus. Fusce aliquet faucibus ultricies. Morbi semper, est id tincidunt gravida, sem arcu adipiscing lacus, ac bibendum nulla leo eu purus. Quisque nec diam sed risus consectetur a ccumsan quis quis nibh. Vestibulum id purus lorem.</p>
      <p>It is a long established fact that a reader will be distracted by the readable content of a page when looking at its layout. The point of using Lorem Ipsum is that it has a more-or-less normal distribution of letters, as opposed to using 'Content here, content here', making it look like readable English. Many desktop publishing packages</p>
    </div>

    <p class="closing">Sincerely,</p>
    <div class="signature" role="img" aria-label="Handwritten signature of Owen Aldren"></div>
  </section>

  <section class="sheet envelope-back">
    <svg class="flap" viewBox="0 0 531 75" aria-hidden="true">
      <path fill="var(--flap)" d="M0 0 H531 L524 30 C518 58 506 74 482 74 H48 C24 74 13 58 7 30 Z"/>
    </svg>
    <div class="brand">
      <span class="brand-dot"></span>
      <span class="brand-name"><span>DR.</span><span>LENNART</span><span>Oral Surgeon</span></span>
    </div>
  </section>

  <section class="sheet envelope-front">
    <div class="brand">
      <span class="brand-dot"></span>
      <span class="brand-name"><span>DR.</span><span>LENNART</span><span>Oral Surgeon</span></span>
    </div>
    <address class="return-address">
      <div class="firm">Dr. Lennart Oral Surgeon</div>
      <div>4120 Tidewater Road</div>
      <div>Juneau, Alaska 99801</div>
    </address>
  </section>

</body>
</html>
```